" A projeto da empresa é ser uma agência de turismo de aventura/esporte com foco em turistas nacionais e estrangeiros que vêm ao Rio de Janeiro e que praticam mountain bike. "

```html
<!DOCTYPE html>
<html lang="pt-BR">
<head>
<meta charset="utf-8">
<title>Serra &amp; Roda — Cartões de visita</title>
<link rel="stylesheet" href="https://fonts.googleapis.com/css2?family=Oswald:wght@400;600&display=swap">
<style>
  :root {
    --stage: #ecebe8;
    --card: #ffffff;
    --mist: #e4e4e4;
    --mist-deep: #d2d2d2;
    --forest: #3e5a3a;
    --forest-soft: #4a6845;
    --ember: #e2672a;
    --ink: #2d2d2d;
  }
  * { box-sizing: border-box; margin: 0; padding: 0; }
  html, body { width: 1200px; height: 1200px; overflow: hidden; }
  body {
    background: var(--stage);
    font-family: "Oswald", sans-serif;
    position: relative;
  }
  .card {
    position: absolute;
    top: 220px;
    width: 460px;
    height: 760px;
    background: var(--card);
    box-shadow: 0 10px 30px rgba(0,0,0,0.15);
    overflow: hidden;
  }
  .card--front { left: 110px; }
  .card--back { left: 630px; }

  .scenery {
    position: absolute;
    left: 0;
    width: 100%;
    background: linear-gradient(180deg, var(--mist) 0%, var(--mist-deep) 100%);
  }
  .scenery--top { top: 0; height: 230px; }
  .scenery--bottom { bottom: 0; height: 200px; background: linear-gradient(0deg, var(--mist) 0%, var(--mist-deep) 100%); }

  .brand {
    position: absolute;
    top: 330px;
    left: 0;
    width: 100%;
    display: flex;
    align-items: center;
    justify-content: center;
    gap: 16px;
  }
  .brand__dot {
    width: 34px;
    height: 34px;
    border-radius: 50%;
    background: var(--forest);
  }
  .brand__name {
    font-weight: 600;
    font-size: 56px;
    letter-spacing: 1px;
    color: var(--forest);
    text-transform: uppercase;
  }

  .back__head {
    position: absolute;
    top: 0; left: 0;
    width: 100%;
    height: 300px;
    background: var(--forest);
    display: flex;
    align-items: center;
    justify-content: center;
  }
  .back__mark {
    font-weight: 600;
    font-size: 44px;
    color: var(--forest-soft);
    text-transform: uppercase;
    letter-spacing: 1px;
  }
  .back__body {
    position: absolute;
    top: 300px; left: 0;
    width: 100%;
    height: 460px;
  }
  .back__scenery {
    position: absolute;
    right: 0; bottom: 0;
    width: 200px; height: 260px;
    background: linear-gradient(180deg, #f1f1f1, var(--mist));
  }
  .contact {
    position: absolute;
    top: 50px; left: 50px;
    list-style: none;
  }
  .contact__item {
    display: flex;
    align-items: center;
    gap: 14px;
    font-size: 19px;
    color: var(--forest);
    text-transform: uppercase;
    margin-bottom: 14px;
  }
  .contact__icon { width: 20px; height: 20px; flex: none; }
  .contact__bullet {
    width: 16px; height: 16px; margin: 0 2px;
    border-radius: 50%; background: var(--ember); flex: none;
  }
  .website {
    position: absolute;
    left: 50px; bottom: 50px;
    color: var(--ink);
    text-transform: uppercase;
    line-height: 1;
  }
  .website__prefix { font-size: 18px; display: block; margin-bottom: 6px; }
  .website__domain { font-size: 34px; font-weight: 600; }
</style>
</head>
<body>
  <section class="card card--front">
    <div class="scenery scenery--top" role="img" aria-label="Faint grey illustration of mountain rocks"></div>
    <div class="brand">
      <span class="brand__dot"></span>
      <span class="brand__name">Serra &amp; Roda</span>
    </div>
    <div class="scenery scenery--bottom" role="img" aria-label="Faint grey illustration of mountain rocks"></div>
  </section>

  <section class="card card--back">
    <div class="back__head">
      <span class="back__mark">Serra &amp; Roda</span>
    </div>
    <div class="back__body">
      <div class="back__scenery" role="img" aria-label="Faint grey illustration of mountain rocks"></div>
      <ul class="contact">
        <li class="contact__item">
          <svg class="contact__icon" viewBox="0 0 24 24"><path fill="#e2672a" d="M6.6 10.8a15 15 0 0 0 6.6 6.6l2.2-2.2c.3-.3.7-.4 1-.2 1.1.4 2.3.6 3.6.6.6 0 1 .4 1 1V20c0 .6-.4 1-1 1A17 17 0 0 1 3 4c0-.6.4-1 1-1h3.5c.6 0 1 .4 1 1 0 1.3.2 2.5.6 3.6.1.3 0 .7-.2 1z"/></svg>
          (00) 0000-0000
        </li>
        <li class="contact__item">
          <svg class="contact__icon" viewBox="0 0 24 24"><rect x="2" y="5" width="20" height="14" rx="2" fill="#e2672a"/><path d="M3 6l9 7 9-7" fill="none" stroke="#fff" stroke-width="1.8"/></svg>
          contato@serraeroda.com
        </li>
        <li class="contact__item"><span class="contact__bullet"></span>/serraerodamtb</li>
        <li class="contact__item"><span class="contact__bullet"></span>/serraerodamtb</li>
        <li class="contact__item">
          <svg class="contact__icon" viewBox="0 0 24 24"><path fill="#e2672a" d="M12 2a7 7 0 0 0-7 7c0 5 7 13 7 13s7-8 7-13a7 7 0 0 0-7-7zm0 9.5A2.5 2.5 0 1 1 12 6.5a2.5 2.5 0 0 1 0 5z"/></svg>
          Rua xxx, xxxx, 00
        </li>
        <li class="contact__item"><span class="contact__icon"></span>Bairro xxx - Cidade - Estado</li>
      </ul>
      <p class="website">
        <span class="website__prefix">www.</span>
        <span class="website__domain">serraerodamtb.com</span>
      </p>
    </div>
  </section>
</body>
</html>
```